Professional business card for beauty services

I need a business card that targets women between the ages of 20-50 looking to get hair styling and makeup done for special occasions. I also provide lash extensions and lash enhancement services. My main focus is bridal work. I want my card to look profesional and bright with a font easy to read. I don't like clutter and I don't want the information to feel overwhelming or like it's too much.
Eye catching would be nice.

Target Market(s)

Women 20-50 years old

Industry/Entity Type

Business

Contact Information for Business Card

www.pennyglowstudio.ca
info@pennyglowstudio.ca
Makeup
Hair styling
Lashes
KissTrue Rep
1 (604) 555-3178

Font styles to use
Serif
Sans Serif

Requirements
Must have
• Logo
• Phone number
• Website
• Email
Nice to have
• Social media info
• IG: @pennyglowstudio.ca
• Facebook: Penny Glow Studio by Marta
• Twitter: @penny_glow

```html
<!DOCTYPE html>
<html lang="en">
<head>
<meta charset="utf-8">
<title>Penny Glow Studio by Marta – Business Card</title>
<link rel="stylesheet" href="https://fonts.googleapis.com/css2?family=Mulish:wght@400;600&display=swap">
<style>
  :root {
    --backdrop: #2a2a2a;
    --card: #ffffff;
    --card-tint: #f1f0ef;
    --ink: #1c1c1c;
    --pink: #f28fb0;
    --pink-soft: #f6b8cc;
    --rule: #f0b3c6;
  }
  * { box-sizing: border-box; margin: 0; padding: 0; }
  html, body { width: 1200px; height: 970px; overflow: hidden; }
  body {
    background: var(--backdrop);
    font-family: "Mulish", "Helvetica Neue", Arial, sans-serif;
    color: var(--ink);
    position: relative;
  }
  .card {
    position: absolute;
    left: 242px;
    width: 731px;
    border-radius: 14px;
    overflow: hidden;
    background:
      radial-gradient(ellipse at 15% 30%, var(--card-tint) 0%, transparent 45%),
      radial-gradient(ellipse at 85% 70%, var(--card-tint) 0%, transparent 50%),
      var(--card);
  }
  .card--front { top: 30px; height: 426px; }
  .card--back { top: 510px; height: 428px; }
  .centered {
    position: absolute;
    left: 0; right: 0;
    text-align: center;
    white-space: nowrap;
  }
  .wordmark {
    font-weight: 400;
    color: var(--ink);
    letter-spacing: 3px;
    text-transform: uppercase;
    line-height: 1.15;
  }
  .card--front .wordmark { top: 100px; font-size: 36px; }
  .card--back .wordmark { top: 212px; font-size: 26px; }
  .wordmark small { display: block; font-size: 0.5em; letter-spacing: 6px; }
  .services { top: 214px; font-size: 21px; }
  .services span { margin: 0 6px; }
  .divider {
    position: absolute;
    left: 36px; right: 36px; top: 247px;
    height: 1px;
    background: var(--rule);
  }
  .contact {
    top: 268px;
    font-size: 21px;
    display: flex;
    justify-content: center;
    align-items: center;
    gap: 12px;
  }
  .contact .sep { margin: 0 8px; }
  .icon-web {
    width: 30px; height: 30px; border-radius: 50%;
    background: var(--pink);
    display: inline-block;
  }
  .phone { top: 323px; font-size: 37px; }
  .portrait {
    position: absolute;
    left: 318px; top: 42px;
    width: 96px; height: 162px;
    border-radius: 48px 48px 20px 20px;
    background: linear-gradient(160deg, #3a3a3a 0%, #9a9a9a 55%, #f4d6df 100%);
  }
  .follow { top: 280px; font-size: 22px; font-weight: 600; }
  .socials {
    position: absolute;
    top: 326px; left: 0; right: 0;
    display: flex;
    justify-content: center;
    gap: 34px;
  }
  .social {
    display: flex;
    flex-direction: column;
    align-items: center;
    gap: 8px;
    font-size: 19px;
    white-space: nowrap;
  }
  .social .dot {
    width: 26px; height: 26px; border-radius: 50%;
    background: var(--pink-soft);
  }
</style>
</head>
<body>
  <section class="card card--front">
    <div class="centered wordmark">Penny Glow Studio<small>by Marta</small></div>
    <div class="centered services">Makeup<span>|</span>Hair styling<span>|</span>Lashes<span>|</span>KissTrue Rep</div>
    <div class="divider"></div>
    <div class="centered contact">
      <svg width="30" height="22" viewBox="0 0 30 22" aria-hidden="true">
        <rect x="1" y="1" width="28" height="20" rx="2" fill="none" stroke="var(--pink)" stroke-width="2"/>
        <path d="M1 2 L15 13 L29 2" fill="none" stroke="var(--pink)" stroke-width="2"/>
      </svg>
      <span>info@pennyglowstudio.ca</span>
      <span class="sep">|</span>
      <span class="icon-web"></span>
      <span>www.pennyglowstudio.ca</span>
    </div>
    <div class="centered phone">1 (604) 555-3178</div>
  </section>

  <section class="card card--back">
    <div class="portrait" role="img" aria-label="Line illustration of a woman with flowing hair and pink lips"></div>
    <div class="centered wordmark">Penny Glow Studio<small>by Marta</small></div>
    <div class="centered follow">Follow us on Social Media</div>
    <div class="socials">
      <div class="social"><span class="dot"></span><span>Penny Glow Studio by Marta</span></div>
      <div class="social"><span class="dot"></span><span>@penny_glow</span></div>
      <div class="social"><span class="dot"></span><span>@pennyglowstudio.ca</span></div>
    </div>
  </section>
</body>
</html>
```